GUARANTEED! Simple website for independent event planner and consultant...

I need a website that is no more than 5 or 6 pages to illustrate who I am and what I can offer to groups who book hotels for meetings and conferences. I have 20 years of experience planning meetings within hotels and I am now ready to go out on my own and help clients choose venues, negotiate contracts and plan effective meetings. I will focus on clients planning meetings in the mountains of Colorado but I am willing to travel as well. I want to work with a person who is collaborative and can direct me on what they need to move the project along quickly. I already have my logo, a hosting site and work e-mail address. Also, I recently hired a photographer to do head shots. Lastly, it important for me to be able to talk on the phone or skype with this person, as needed and I must be able to make changes to my site down the road when necessary...

Target Market(s)

Corporate Groups

Industry/Entity Type

Event Planning

Coding

Coded - Design and coding required

Number of Pages Required

5+ page

Font styles to use
Sans Serif

Requirements
Must have
• About me page, event planning services offered page, task force and consulting work page, testimonials page, page for blogs, page to contact me/request a proposal. May need advice on what else I need...
Nice to have
• I want it to look sharp and professional. I want people to look at my site and know immediately that they can trust me and the work I can do.
• I don't want it to look like it is over the top as I am not a HUGE company but I do want it to be professional and easy to view and navigate.
Should not have
• Bright colors
• My logo is bright orange and black. I have also used dark grey and orange. See below:
• Orange:
• C = 0
• M = 64
• Y = 100
• K = 0
• Gray:
• C = 67
• M = 60
• Y = 59
• K = 45
• Font: Gotham Book and Gotham Bold

```html
<!DOCTYPE html>
<html lang="en">
<head>
<meta charset="utf-8">
<title>Harlow Event Management</title>
<link rel="stylesheet" href="https://fonts.googleapis.com/css2?family=Montserrat:wght@400;500;600;700&family=Lato:wght@400;700&display=swap">
<style>
:root{
  --orange:#f37b24;
  --orange-soft:#e8793a;
  --charcoal:#454545;
  --charcoal-dark:#353535;
  --paper:#ececec;
  --ink:#2b2b2b;
  --white:#ffffff;
}
*{margin:0;padding:0;box-sizing:border-box}
html,body{width:1200px;height:2601px;overflow:hidden}
body{position:relative;background:var(--paper);font-family:"Lato",sans-serif;color:var(--ink)}
.abs{position:absolute}
.heading{font-family:"Montserrat",sans-serif;font-weight:700;letter-spacing:1px;font-size:28px;text-align:center;width:100%;color:var(--charcoal)}
.heading span{color:var(--orange)}
.dots{display:flex;gap:8px;justify-content:center;width:100%}
.dots i{width:9px;height:9px;border-radius:50%;background:var(--orange);display:block}
.dots i.mid{width:12px;height:12px;background:var(--charcoal);margin-top:-1.5px}
.arrow{width:24px;height:40px}

/* header */
.topbar{left:0;top:0;width:1200px;height:99px;background:var(--charcoal)}
.brand{left:134px;top:22px;font-family:"Montserrat",sans-serif;font-weight:600;color:var(--orange);font-size:21px;line-height:26px;text-transform:uppercase}
.phone{left:625px;top:30px;display:flex;align-items:center;gap:22px;color:var(--white);font-family:"Montserrat",sans-serif;font-size:20px}
.phone .ring{width:40px;height:40px;border-radius:50%;background:var(--orange);display:flex;align-items:center;justify-content:center}
.proposal{left:845px;top:29px;width:225px;height:40px;border-radius:20px;background:var(--orange);color:var(--white);font-family:"Montserrat",sans-serif;font-weight:600;font-size:17px;display:flex;align-items:center;justify-content:center;gap:10px}
.mainnav{left:0;top:99px;width:1200px;height:48px;background:var(--orange)}
.mainnav ul{list-style:none;display:flex;gap:34px;position:absolute;left:134px;top:15px;font-family:"Montserrat",sans-serif;font-weight:600;font-size:13.5px;color:var(--white);letter-spacing:.3px}
.mainnav li.active{border-bottom:3px solid var(--white);padding-bottom:11px}

/* hero */
.hero{left:0;top:147px;width:1200px;height:498px;background:linear-gradient(180deg,#d96a7e 0%,#c85a7a 35%,#8e4a5a 70%,#7a4a4e 100%)}
.hero-person{left:798px;top:173px;width:312px;height:472px;background:linear-gradient(180deg,#d9b28e 0%,#e07a5a 45%,#222 75%,#1b1b1b 100%);border-radius:140px 140px 0 0;opacity:.9}
.hero-caption{left:173px;top:369px;width:642px;height:96px;background:rgba(40,20,30,.55);color:var(--white);font-family:"Lato",sans-serif;font-size:27px;line-height:37px;padding:11px 18px}

/* services */
.services{left:0;top:645px;width:1200px;height:354px}
.service{top:140px;width:200px;text-align:center;font-family:"Montserrat",sans-serif;font-weight:600;font-size:17px;line-height:24px;color:var(--ink)}
.service .circle{width:108px;height:108px;border-radius:50%;border:2px solid var(--orange);background:var(--white);margin:0 auto 22px;display:flex;align-items:center;justify-content:center}
.service.small{font-size:15px;line-height:20px}

/* about */
.about{left:0;top:999px;width:1200px;height:328px;background:var(--orange-soft)}
.about-photo{left:104px;top:24px;width:173px;height:304px;background:linear-gradient(180deg,#e2c29a 0%,#cfc6bd 40%,#6f7f8e 100%);border-radius:80px 80px 0 0}
.about-title{left:302px;top:56px;font-family:"Montserrat",sans-serif;font-weight:700;font-size:28px;color:var(--white);letter-spacing:1px}
.about-rule{left:302px;top:113px;width:770px;height:1px;background:rgba(255,255,255,.45)}
.about-dots{left:302px;top:107px;display:flex;gap:8px}
.about-dots i{width:9px;height:9px;border-radius:50%;background:var(--white)}
.about-dots i.mid{width:12px;height:12px;background:var(--charcoal);margin-top:-1.5px}
.about-lead{left:302px;top:143px;width:770px;font-weight:700;font-size:14.5px;line-height:24px;color:var(--white)}
.about-body{left:302px;top:205px;width:770px;font-size:14px;line-height:26px;color:#fbe8dc}
.about-body u{color:var(--white);font-weight:700}

/* gallery */
.gallery{left:0;top:1327px;width:1200px;height:506px}
.tile{width:201px;height:132px;border:3px solid var(--white);box-shadow:0 1px 4px rgba(0,0,0,.25)}
.tile b{position:absolute;left:4px;bottom:8px;background:rgba(255,255,255,.8);font-weight:400;font-size:12.5px;padding:2px 6px;color:var(--ink)}

/* reviews + blog */
.dark{left:0;top:1833px;width:1200px;height:393px;background:var(--charcoal)}
.col-title{font-family:"Montserrat",sans-serif;font-weight:700;font-size:22px;color:var(--orange);letter-spacing:.5px}
.col-rule{height:1px;background:#777}
.nav-pair{color:var(--white);font-size:16px;font-family:"Montserrat",sans-serif}
.avatar{border-radius:50%;border:3px solid var(--white);background:linear-gradient(160deg,#9a7b6a,#5a463e)}
.quote{font-size:13.5px;line-height:22px;color:#eee}
.readmore{font-size:12px;font-style:italic;color:var(--orange)}
.reviewer{font-weight:700;font-size:13px;color:var(--white);text-align:center}
.post{left:706px;width:360px;font-size:12.5px;line-height:19.5px;color:#eee}
.post strong{color:var(--white)}

/* contact */
.map{left:0;top:2226px;width:1200px;height:278px;background:linear-gradient(135deg,#e6e4de 0%,#dcdad2 50%,#e8e6df 100%)}
.card{background:var(--orange);border-radius:8px;color:var(--white)}
.card h3{font-family:"Montserrat",sans-serif;font-weight:700;font-size:16px;color:var(--ink);margin-bottom:12px}
.contact-card{left:134px;top:2272px;width:286px;height:216px;padding:20px 24px}
.contact-card li{list-style:none;display:flex;gap:12px;font-size:13px;line-height:18px;margin-bottom:8px}
.contact-card svg{flex:none;margin-top:2px}
.center-brand{left:460px;top:2320px;width:280px;text-align:center;font-family:"Montserrat",sans-serif;font-weight:600;color:var(--orange);font-size:24px;line-height:28px;text-transform:uppercase}
.social{left:530px;top:2413px;display:flex;gap:12px}
.social i{width:26px;height:26px;border-radius:50%;display:block}
.inquiry{left:822px;top:2272px;width:246px;height:199px;padding:16px 20px}
.inquiry h3{margin-bottom:8px}
.field{background:#fde9d6;height:22px;margin-bottom:6px;font-size:11.5px;padding:4px 8px;color:var(--ink)}
.field.msg{height:46px}
.submit{display:inline-block;background:var(--white);color:var(--ink);font-family:"Montserrat",sans-serif;font-weight:700;font-size:11.5px;padding:4px 10px;margin-top:2px}

/* footer */
.footer{left:0;top:2504px;width:1200px;height:97px;background:var(--charcoal-dark)}
.footer ul{list-style:none;display:flex;justify-content:center;position:absolute;top:30px;width:100%;font-family:"Montserrat",sans-serif;font-size:13px;color:#ddd}
.footer li{padding:0 18px;border-left:1px solid #777}
.footer li:first-child{border-left:none}
.copyright{position:absolute;top:62px;width:100%;text-align:center;font-size:13px;color:#bbb}
</style>
</head>
<body>

<header>
  <div class="abs topbar"></div>
  <div class="abs brand">Harlow<br>Event Management</div>
  <div class="abs phone">
    <span class="ring"><svg width="20" height="20" viewBox="0 0 24 24"><path fill="#fff" d="M6.6 10.8a15 15 0 0 0 6.6 6.6l2.2-2.2c.3-.3.7-.4 1-.2 1.1.4 2.3.6 3.6.6.6 0 1 .4 1 1V20c0 .6-.4 1-1 1A17 17 0 0 1 3 4c0-.6.4-1 1-1h3.5c.6 0 1 .4 1 1 0 1.3.2 2.5.6 3.6.1.3 0 .7-.2 1z"/></svg></span>
    555 010 2040
  </div>
  <div class="abs proposal">
    <svg width="18" height="18" viewBox="0 0 24 24"><rect x="3" y="5" width="14" height="16" fill="none" stroke="#fff" stroke-width="2"/><path d="M10 14l9-9 2 2-9 9h-2z" fill="#fff"/></svg>
    Request A Proposal
  </div>
  <nav class="abs mainnav">
    <ul>
      <li class="active">HOME</li><li>ABOUT ME</li><li>EVENT PLANNING SERVICES</li><li>TASK FORCE &amp; CONSULTING</li><li>TESTIMONIALS</li><li>BLOG</li><li>CONTACT ME</li>
    </ul>
  </nav>
</header>

<section>
  <div class="abs hero" role="img" aria-label="Photo of a decorated banquet ballroom with round tables"></div>
  <div class="abs hero-person" role="img" aria-label="Portrait of the event planner in a black blazer"></div>
  <div class="abs hero-caption">I Am An Event Planner And Consultant Working Independently With Over 20 Years of Experience</div>
  <svg class="abs arrow" style="left:57px;top:353px" viewBox="0 0 24 40"><path d="M20 2L4 20l16 18" fill="none" stroke="#fff" stroke-width="3"/></svg>
  <svg class="abs arrow" style="left:1119px;top:353px" viewBox="0 0 24 40"><path d="M4 2l16 18L4 38" fill="none" stroke="#fff" stroke-width="3"/></svg>
</section>

<section class="abs services">
  <h2 class="abs heading" style="top:48px"><span>SERVICES</span> OFFERED</h2>
  <div class="abs dots" style="top:100px"><i></i><i class="mid"></i><i></i></div>
  <svg class="abs arrow" style="left:88px;top:180px" viewBox="0 0 24 40"><path d="M18 8L6 20l12 12" fill="none" stroke="#555" stroke-width="3"/></svg>
  <svg class="abs arrow" style="left:1098px;top:180px" viewBox="0 0 24 40"><path d="M6 8l12 12L6 32" fill="none" stroke="#555" stroke-width="3"/></svg>

  <div class="abs service" style="left:106px;top:140px"><div class="circle"><svg width="56" height="44" viewBox="0 0 56 44"><path d="M4 22a24 18 0 0 1 48 0z" fill="#333"/><rect x="4" y="22" width="48" height="18" fill="#333"/><g fill="#fff"><rect x="10" y="26" width="5" height="14"/><rect x="19" y="26" width="5" height="14"/><rect x="28" y="26" width="5" height="14"/><rect x="37" y="26" width="5" height="14"/></g></svg></div>Site Inspections &amp;<br>Venue Selection</div>
  <div class="abs service" style="left:323px;top:140px"><div class="circle"><svg width="58" height="44" viewBox="0 0 58 44"><circle cx="18" cy="8" r="6" fill="#333"/><circle cx="40" cy="8" r="6" fill="#333"/><path d="M8 28v-8c0-4 4-6 10-6s10 2 10 6v8zM30 28v-8c0-4 4-6 10-6s10 2 10 6v8z" fill="#333"/><rect x="4" y="26" width="50" height="5" fill="#333"/><rect x="12" y="31" width="4" height="12" fill="#333"/><rect x="42" y="31" width="4" height="12" fill="#333"/></svg></div>Contract<br>Negotiations</div>
  <div class="abs service" style="left:516px;top:140px"><div class="circle"><svg width="56" height="48" viewBox="0 0 56 48"><circle cx="28" cy="24" r="16" fill="none" stroke="#333" stroke-width="4"/><circle cx="28" cy="24" r="9" fill="#333"/><path d="M4 4v14M8 4v14M12 4v14M4 18h8M8 18v26" stroke="#333" stroke-width="2.5" fill="none"/><path d="M50 4c-4 4-4 14 0 16v24" stroke="#333" stroke-width="3.5" fill="none"/></svg></div>Food and<br>Beverage</div>
  <div class="abs service" style="left:715px;top:140px"><div class="circle"><svg width="52" height="50" viewBox="0 0 52 50"><rect x="4" y="8" width="36" height="34" rx="3" fill="none" stroke="#333" stroke-width="3"/><path d="M4 16h36M12 4v8M32 4v8" stroke="#333" stroke-width="3"/><g fill="#333"><rect x="10" y="22" width="5" height="4"/><rect x="19" y="22" width="5" height="4"/><rect x="28" y="22" width="5" height="4"/><rect x="10" y="31" width="5" height="4"/><rect x="19" y="31" width="5" height="4"/></g><circle cx="38" cy="38" r="10" fill="#fff" stroke="#333" stroke-width="3"/><path d="M38 32v6h5" stroke="#333" stroke-width="2.5" fill="none"/></svg></div>Agenda Creation &amp;<br>Progam Planning</div>
  <div class="abs service small" style="left:914px;top:140px"><div class="circle"><svg width="54" height="46" viewBox="0 0 54 46"><path d="M20 6a18 18 0 1 0 0 34" fill="none" stroke="#333" stroke-width="3"/><path d="M20 14a10 10 0 1 0 0 18" fill="none" stroke="#333" stroke-width="3"/><rect x="22" y="16" width="16" height="14" fill="#333"/><path d="M38 20l12-8v22l-12-8z" fill="#333"/></svg></div>AudioVisual<br>Expertise</div>
</section>

<section class="abs about">
  <div class="abs about-photo" role="img" aria-label="Head shot of the event planner in a grey cardigan"></div>
  <h2 class="abs about-title">ABOUT ME</h2>
  <div class="abs about-rule"></div>
  <div class="abs about-dots"><i></i><i class="mid"></i><i></i></div>
  <p class="abs about-lead">Harlow Event Management specializes in event management for associations, corporations, not for profit companies and personal social events of all sizes in the state of Colorado</p>
  <p class="abs about-body">After a successful 20+ year career coordinating events in the resort community of Vail I am now providing her skills on the other side of the table. When you hire Harlow Event Management you are hiring a company who is intimately familiar with the inner-workings of hotels, resorts and off-site hospitality venues. <u>Read More ...</u></p>
</section>

<section class="abs gallery">
  <h2 class="abs heading" style="top:50px"><span>WORK</span> GALLERY</h2>
  <div class="abs dots" style="top:102px"><i></i><i class="mid"></i><i></i></div>
  <svg class="abs arrow" style="left:82px;top:284px" viewBox="0 0 24 40"><path d="M18 8L6 20l12 12" fill="none" stroke="#555" stroke-width="3"/></svg>
  <svg class="abs arrow" style="left:1091px;top:284px" viewBox="0 0 24 40"><path d="M6 8l12 12L6 32" fill="none" stroke="#555" stroke-width="3"/></svg>

  <div class="abs tile" style="left:134px;top:150px;background:linear-gradient(160deg,#b32a1e,#e8a43a 60%,#7a1d12)" role="img" aria-label="Event photo: red and gold stage decor"><b>Lorem ipsum</b></div>
  <div class="abs tile" style="left:376px;top:150px;background:linear-gradient(160deg,#e0672a,#f2b24a 50%,#c8401e)" role="img" aria-label="Event photo: orange draped wedding aisle"><b>Lorem ipsum</b></div>
  <div class="abs tile" style="left:619px;top:150px;background:linear-gradient(160deg,#6c4fd0,#b7a6f0 50%,#4b2f9a)" role="img" aria-label="Event photo: purple lit banquet hall"><b>Lorem ipsum</b></div>
  <div class="abs tile" style="left:862px;top:150px;background:linear-gradient(160deg,#5a1a22,#d9c7b8 55%,#3a2a28)" role="img" aria-label="Event photo: stage with red curtains and white seating"><b>Lorem ipsum</b></div>
  <div class="abs tile" style="left:134px;top:312px;background:linear-gradient(160deg,#8a4a12,#e2b05a 50%,#6a3410)" role="img" aria-label="Event photo: warm gold ballroom"><b>Lorem ipsum</b></div>
  <div class="abs tile" style="left:376px;top:312px;background:linear-gradient(160deg,#a88a62,#e8d8b8 50%,#8a6c4a)" role="img" aria-label="Event photo: banquet tables with white linen"><b>Lorem ipsum</b></div>
  <div class="abs tile" style="left:619px;top:312px;background:linear-gradient(160deg,#c83a2a,#f0d8c8 50%,#6a9a5a)" role="img" aria-label="Event photo: tent reception with red lanterns"><b>Lorem ipsum</b></div>
  <div class="abs tile" style="left:862px;top:312px;background:linear-gradient(160deg,#3a1a6a,#b04ac8 50%,#2a1050)" role="img" aria-label="Event photo: purple lit conference room"><b>Lorem ipsum</b></div>
</section>

<section class="abs dark">
  <h2 class="abs col-title" style="left:134px;top:43px">CUSTOMER REVIEWS</h2>
  <span class="abs nav-pair" style="left:548px;top:44px">&lsaquo; &rsaquo;</span>
  <div class="abs col-rule" style="left:134px;top:80px;width:450px"></div>

  <div class="abs avatar" style="left:137px;top:107px;width:76px;height:76px" role="img" aria-label="Reviewer portrait"></div>
  <div class="abs reviewer" style="left:137px;top:193px;width:76px">Lena</div>
  <p class="abs quote" style="left:238px;top:98px;width:330px">&ldquo; Lorem ipsum dolor sit amet, consecerertetu ew adipiscing ir elit, sed diam nonummy nibh euismod er tincidunt ut laore ereeit dolore magna aliquam &rdquo;</p>
  <span class="abs readmore" style="left:238px;top:178px">Read more...</span>

  <p class="abs quote" style="left:134px;top:236px;width:330px">&ldquo; Lorem ipsum dolor sit amet, consecerertetu ew adipiscing ir elit, sed diam nonummy nibh euismod er tincidunt ut laore ereeit dolore magna aliquam &rdquo;</p>
  <span class="abs readmore" style="left:134px;top:318px">Read more...</span>
  <div class="abs avatar" style="left:500px;top:231px;width:76px;height:76px" role="img" aria-label="Reviewer portrait"></div>
  <div class="abs reviewer" style="left:500px;top:318px;width:76px">Dana</div>

  <h2 class="abs col-title" style="left:621px;top:43px">LATEST BLOG POST</h2>
  <span class="abs nav-pair" style="left:1036px;top:44px">&lsaquo; &rsaquo;</span>
  <div class="abs col-rule" style="left:621px;top:80px;width:445px"></div>

  <div class="abs avatar" style="left:621px;top:88px;width:66px;height:66px" role="img" aria-label="Blog thumbnail: event guests"></div>
  <p class="abs post" style="top:92px"><strong>Lorem ipsum dolor sit amet .</strong><br>Lorem ipsum dolor sit amet, consecerertetuer adipiscing e erelit, sed diam nonummy nibh euismod tincidunt ut .</p>
  <div class="abs avatar" style="left:621px;top:177px;width:66px;height:66px" role="img" aria-label="Blog thumbnail: speaker"></div>
  <p class="abs post" style="top:181px"><strong>Lorem ipsum dolor sit amet .</strong><br>Lorem ipsum dolor sit amet, consecerertetuer adipiscing e erelit, sed diam nonummy nibh euismod tincidunt ut .</p>
  <div class="abs avatar" style="left:621px;top:265px;width:66px;height:66px" role="img" aria-label="Blog thumbnail: evening reception"></div>
  <p class="abs post" style="top:269px"><strong>Lorem ipsum dolor sit amet .</strong><br>Lorem ipsum dolor sit amet, consecerertetuer adipiscing e ereli wet, sed diam nonummy nibh euismod tincidunt ut .</p>
</section>

<section>
  <div class="abs map" role="img" aria-label="Street map of the office location"></div>
  <div class="abs card contact-card">
    <h3>CONTACT DETAILS</h3>
    <ul>
      <li><svg width="12" height="16" viewBox="0 0 12 16"><path d="M6 0a6 6 0 0 1 6 6c0 4-6 10-6 10S0 10 0 6a6 6 0 0 1 6-6z" fill="#fff"/><circle cx="6" cy="6" r="2" fill="#f37b24"/></svg>Lorem quip ex earmodoe nseq<br>autem vel eum iriure dolor</li>
      <li><svg width="14" height="10" viewBox="0 0 14 10"><rect width="14" height="10" fill="#fff"/><path d="M0 0l7 6 7-6" fill="none" stroke="#f37b24"/></svg>info@harloweventmanagement.com</li>
      <li><svg width="12" height="12" viewBox="0 0 24 24"><path fill="#fff" d="M6.6 10.8a15 15 0 0 0 6.6 6.6l2.2-2.2c.3-.3.7-.4 1-.2 1.1.4 2.3.6 3.6.6.6 0 1 .4 1 1V20c0 .6-.4 1-1 1A17 17 0 0 1 3 4c0-.6.4-1 1-1h3.5c.6 0 1 .4 1 1 0 1.3.2 2.5.6 3.6.1.3 0 .7-.2 1z"/></svg>555 010 2040</li>
      <li><svg width="12" height="12" viewBox="0 0 12 12"><rect x="1" y="3" width="10" height="8" fill="#fff"/><rect x="3" y="0" width="6" height="4" fill="#fff"/></svg>555 010 2040</li>
    </ul>
  </div>
  <div class="abs center-brand">Harlow<br>Event Management</div>
  <div class="abs social"><i style="background:#3b5a99"></i><i style="background:#1f7bb6"></i><i style="background:#2aa3e0"></i><i style="background:#d9483b"></i></div>
  <div class="abs card inquiry">
    <h3>QUICK INQUIRY</h3>
    <div class="field">Name</div>
    <div class="field">Email</div>
    <div class="field msg">Message</div>
    <span class="submit">SUBMIT</span>
  </div>
</section>

<footer class="abs footer">
  <ul><li>HOME</li><li>ABOUT ME</li><li>EVENT PLANNING SERVICES</li><li>TASK FORCE &amp; CONSULTING</li><li>TESTIMONIALS</li><li>BLOG</li><li>CONTACT ME</li></ul>
  <p class="copyright">Copyright &copy; 2017 Harlow Event Management. All Right Reserved.</p>
</footer>

</body>
</html>
```